Lawyer Needs New Atypical Stationery Design With Gravitas

I need new stationery (letterhead, envelopes, note pads, maybe business cards) for my law office. Although I work by myself, for myself, I need stationery that conveys strength, stability, and gravitas. I would also like a design that makes the end user think: "This is unique. I've never seen letterhead like this before." Most importantly, it should not look like many lawyers' letterhead, meaning no scales of justice. My current letterhead (attached) has my name and "Attorney at Law" on it; however, I would like to transition to "MERIX | LAW" or something like that with the new letterhead. Lastly, I would like an envelope design that is not the standard #10 envelope with a triangular back flap, maybe a square flap or something in the style or design that also makes people stop and think "That's different from anything I've seen before."

```html
<!DOCTYPE html>
<html lang="en">
<head>
<meta charset="utf-8">
<title>Adrian Merix – Letterhead</title>
<link rel="stylesheet" href="https://fonts.googleapis.com/css2?family=Montserrat:wght@700&family=Source+Sans+3:wght@400;600&display=swap">
<style>
  :root {
    --bg: #5c5c5c;
    --paper: #f7f7f7;
    --paper-shade: #ebebeb;
    --tri-light: #e2e2e2;
    --tri-mid: #d9d9d9;
    --ink: #34405e;
    --gold: #d4a72c;
    --gold-soft: #e8cf8a;
    --black: #111111;
    --black-2: #2b2b2b;
  }
  * { box-sizing: border-box; margin: 0; padding: 0; }
  html, body { width: 1200px; height: 960px; overflow: hidden; background: var(--bg); }
  .canvas { position: relative; width: 1200px; height: 960px; }
  .letterhead {
    position: absolute; left: 280px; top: 27px; width: 640px; height: 906px;
    background: linear-gradient(160deg, var(--paper-shade), var(--paper) 45%);
    overflow: hidden; color: var(--ink);
    font-family: "Source Sans 3", sans-serif;
    box-shadow: 0 10px 30px rgba(0,0,0,.35);
  }
  .frame-art { position: absolute; inset: 0; }
  .brand { position: absolute; top: 165px; right: 40px; display: flex; align-items: center; gap: 12px; }
  .brand-dot { width: 34px; height: 34px; border-radius: 50%; background: var(--gold); }
  .brand-name { font-size: 26px; font-weight: 600; letter-spacing: 1px; color: var(--ink); }
  .brand-tag { position: absolute; top: 205px; right: 40px; font-size: 11px; letter-spacing: 6px; color: var(--ink); }
  .letter-date { position: absolute; top: 270px; right: 40px; font-size: 16px; }
  .letter-body { position: absolute; top: 296px; left: 60px; width: 500px; }
  .headline { font-family: "Montserrat", sans-serif; font-weight: 700; font-size: 28px; margin-bottom: 12px; }
  .letter-body p { font-size: 15px; line-height: 1.42; margin-bottom: 18px; }
  .sign-off { margin-top: 6px; line-height: 1.3; }
  .sign-name { font-size: 15px; font-weight: 600; letter-spacing: .5px; }
  .sign-role { font-size: 12px; color: #9a8a5a; font-style: italic; }
  .sign-line { font-size: 12px; color: var(--gold); }
  .contact { position: absolute; top: 790px; left: 330px; list-style: none; font-size: 12px; }
  .contact li { display: flex; align-items: flex-start; gap: 8px; margin-bottom: 6px; }
  .contact li.phone { font-size: 15px; }
  .contact svg { flex: none; margin-top: 1px; }
</style>
</head>
<body>
<div class="canvas">
  <section class="letterhead">
    <svg class="frame-art" viewBox="0 0 640 906" width="640" height="906">
      <defs>
        <linearGradient id="blackBand" x1="0" y1="0" x2="1" y2="1">
          <stop offset="0" stop-color="#2b2b2b"/><stop offset="1" stop-color="#0d0d0d"/>
        </linearGradient>
        <linearGradient id="dotField" x1="0" y1="0" x2="1" y2="1">
          <stop offset="0" stop-color="#e8cf8a" stop-opacity=".45"/><stop offset="1" stop-color="#e8cf8a" stop-opacity="0"/>
        </linearGradient>
      </defs>
      <polygon points="300,235 640,90 640,160" fill="var(--tri-light)"/>
      <polygon points="460,260 640,170 640,320 560,360" fill="var(--tri-mid)" opacity=".7"/>
      <polygon points="560,380 640,350 640,520" fill="var(--tri-light)"/>
      <polygon points="0,0 640,0 640,60 0,250" fill="url(#blackBand)"/>
      <polygon points="0,0 420,0 0,160" fill="#1c1c1c" opacity=".6"/>
      <line x1="0" y1="222" x2="640" y2="40" stroke="var(--gold)" stroke-width="2"/>
      <line x1="60" y1="190" x2="640" y2="58" stroke="var(--gold)" stroke-width="1"/>
      <polygon points="420,906 640,800 640,906" fill="var(--tri-light)"/>
      <polygon role="img" aria-label="Fine gold dot pattern" points="0,780 0,906 240,906" fill="url(#dotField)"/>
      <polygon points="0,790 0,906 110,906" fill="url(#blackBand)"/>
      <line x1="0" y1="804" x2="100" y2="906" stroke="var(--gold)" stroke-width="1.5"/>
      <polygon points="330,906 640,870 640,906" fill="url(#blackBand)"/>
      <line x1="300" y1="900" x2="640" y2="866" stroke="var(--gold)" stroke-width="1"/>
    </svg>

    <div class="brand"><span class="brand-dot"></span><span class="brand-name">ADRIAN MERIX</span></div>
    <div class="brand-tag">ATTORNEY AT LAW</div>
    <div class="letter-date">Spain, January 13 2024</div>

    <article class="letter-body">
      <h1 class="headline">Headline</h1>
      <p>Lorem ipsum dolor sit amet, consectetuer adipiscing elit, sed diam nonummy nibh euismod tincidunt ut laoreet dolore magna aliquam erat volutpat. Ut wisi enim ad minim veniam, quis nostrud exerci tation ullamcorper suscipit lobortis nisl ut aliquip ex ea commodo consequat. Duis autem vel eum iriure dolor in hendrerit in vulputate velit esse molestie consequat, vel illum dolore eu feugiat nulla facilisis at vero eros et</p>
      <p>Lorem ipsum dolor sit amet, consectetuer adipiscing elit, sed diam nonummy nibh euismod tincidunt ut laoreet dolore magna aliquam erat volutpat. Ut wisi enim ad minim veniam, quis nostrud exerci tation ullamcorper suscipit lobortis nisl ut aliquip ex ea commodo consequat. Duis autem vel eum iriure dolor in hendrerit in vulputate velit esse molestie consequat, vel illum dolore eu feugiat nulla facilisis at vero eros et</p>
      <p>Lorem ipsum dolor sit amet, consectetuer adipiscing elit, sed diam nonummy nibh euismod tincidunt ut laoreet dolore magna aliquam erat volutpat. Ut wisi enim ad minim veniam, quis nostrud exerci tation ullamcorper.</p>
      <div class="sign-off">
        <div class="sign-name">ADRIAN MERIX</div>
        <div class="sign-role">Lawyer</div>
        <div class="sign-line">Signature ..........</div>
      </div>
    </article>

    <ul class="contact">
      <li class="phone">
        <svg width="16" height="16" viewBox="0 0 16 16"><circle cx="8" cy="8" r="8" fill="var(--gold)"/><path d="M5 4.5l1.5-.5 1 2-1 .8a5 5 0 0 0 2.7 2.7l.8-1 2 1-.5 1.5c-3.5 0-6.5-3-6.5-6.5z" fill="#fff"/></svg>
        (555) 014-3382</li>
      <li>
        <svg width="16" height="16" viewBox="0 0 16 16"><circle cx="8" cy="8" r="8" fill="var(--gold)"/><rect x="4" y="5" width="8" height="6" fill="none" stroke="#fff"/><path d="M4 5l4 3 4-3" fill="none" stroke="#fff"/></svg>
        ADRIAN@ADRIANMERIX.com</li>
      <li>
        <svg width="16" height="16" viewBox="0 0 16 16"><circle cx="8" cy="8" r="8" fill="var(--gold)"/><path d="M8 3.5a3 3 0 0 1 3 3c0 2-3 5.5-3 5.5S5 8.5 5 6.5a3 3 0 0 1 3-3z" fill="#fff"/><circle cx="8" cy="6.5" r="1" fill="var(--gold)"/></svg>
        <span>CEDAR PARK HUNDRED<br>CA 90000-1234</span></li>
    </ul>
  </section>
</div>
</body>
</html>
```